Need a clean & modern homepage for an education site + opportunity for longer term work

Thanks for viewing our project. We are excited about this new website and we hope that we might build a relationship with designers as we work on this project. I provided quite a few details and requirements to help you more quickly create a design that meets our needs.
Who we are:
We are a website that discusses the importance of Quillhaven and provides a directory of college programs.
What we need:
A homepage that meets the below requirements and is inspired by the examples provided
Definition of accredited:
ac·cred·it·ed [uh-kred-i-tid] adj.
1. officially recognized as meeting the essential requirements, as of academic excellence: accredited schools.
2. provided with official credentials, as by a government: an accredited diplomatic representative.
3. accepted as authoritative: an accredited theory.
Overall look and feel for the homepage:
- Clean, simple and modern
- Limited (or zero) pictures
- Utilize color blocks with text
- A trend seems to be longer vertical length homepages with lots of whitespace. I generally like this trend as long as the page is not way to tall.
Inspirations: Sites that have a similar look and feel to what I need.
http://lernvista.org/
http://www.campusmetrix.com/colleges/orlen-university/
http://quietmarrow.org/
http://www.velmoratalent.com/
http://www.pluvo.com/
http://sketches.zumo.com/
Items to be included on the homepage. Details below on each item.
- Top navigation
- Logo: Please leave a blank area for a logo. The logo has not been designed.
- Simple graphic/color block at the top that highlights a definition of “Accredited” – the definition should be formatted like it is being copy/pasted from a dictionary.
- Space for a video and small (50 word) written description of the video. You can use placeholder text.
- One section with 3 Paragraphs of content (each paragraph around 100 words) with a header at the top. You can use placeholder text but please create the formatting. At the end of the 3 paragraphs please have a “Read More” Note this shouldn't be 3 separate paragraphs with three read mores - it is 3 paragraphs with one read more at the end.
- An area with the header “Search Colleges by State” that has anchor text links to all 50 states.
Top navigation:
- Home
- States – with a subnav dropdown that includes all 50 US states.
- Programs – with a subnav dropdown that includes program titles (list below)
- Degrees - with a subnav dropdown that includes 5 degree levels (list below)
- Accreditation – no subnav
- Rankings – no subnav
- Resources – no subnav
Footer
- Link to about us, privacy, and a copyright www.url.com
Programs List for sub navigation
Accounting
Art
Bible
Business
Criminal Justice
Design
Engineering
English
Law
LPN to RN
Management
Math
MBA
MPH
Medical Assisting
Military
Nursing
Occupational Therapy
Paralegal
Psychology
Pharmacy
RN to BSN
Radiology
Social Work
Sonography
Degrees list for sub navigation
Certificate
Associate
Bachelors
Masters
PhD
Thanks so much - looking forward to working with you!

```html
<!DOCTYPE html>
<html lang="en">
<head>
<meta charset="utf-8">
<title>Quillhaven — Home</title>
<link rel="stylesheet" href="https://fonts.googleapis.com/css2?family=Aleo:wght@300;400;700&family=Open+Sans:wght@300;400;600&display=swap">
<style>
:root{
  --teal:#1aa386;
  --header-bg:#eceff0;
  --navy:#34495e;
  --footer:#3d4850;
  --red:#e74c3c;
  --ink:#2d3e3a;
  --nav-ink:#3a3f42;
  --white:#ffffff;
  --muted:#9aa0a3;
}
*{box-sizing:border-box;margin:0;padding:0}
html,body{width:1106px;height:1200px;overflow:hidden;background:var(--white)}
body{font-family:"Aleo",Georgia,serif;color:var(--ink);position:relative}
a{color:inherit;text-decoration:none}

.topbar{height:28px;background:var(--teal);color:var(--white);font-family:"Open Sans",Arial,sans-serif;font-size:12px}
.topbar-inner{position:absolute;right:152px;top:0;height:28px;display:flex;align-items:center}
.topbar-link{padding:0 11px;line-height:28px;border-right:1px solid rgba(255,255,255,.25)}
.topbar-link:last-of-type{border-right:none}
.keep{padding-left:17px;margin-right:13px}
.social{display:flex;gap:5px}
.social span{width:20px;height:20px;border:1.5px solid var(--white);border-radius:50%}

.site-header{position:absolute;top:28px;left:0;width:1106px;height:75px;background:var(--header-bg)}
.brand{position:absolute;left:151px;top:25px;font-family:"Aleo",Georgia,serif;font-weight:700;font-size:17px;color:var(--teal);letter-spacing:-.3px}
.main-nav{position:absolute;left:407px;top:0;display:flex;height:75px;font-family:"Open Sans",Arial,sans-serif;font-size:13.4px;color:var(--nav-ink)}
.main-nav a{line-height:75px;padding:0 10px;margin-right:4px}
.main-nav a.active{background:var(--teal);color:var(--white);font-weight:600;width:58px;text-align:center;padding:0}

.definition{position:absolute;left:151px;top:132px;width:343px;height:304px;background:var(--teal);color:var(--white);padding:36px 20px 0 36px}
.def-word{font-weight:700;font-size:23.5px;letter-spacing:-1.9px;line-height:1.1;white-space:nowrap}
.def-pos{font-weight:700;font-size:16px;margin-top:5px}
.def-list{list-style:none;margin-top:24px}
.def-list li{display:flex;margin-bottom:20px}
.def-num{font-family:"Open Sans",Arial,sans-serif;font-weight:300;font-size:33px;line-height:30px;width:28px;flex:none}
.def-text{font-size:11.4px;line-height:15px;font-weight:400;padding-top:1px}

.video{position:absolute;left:526px;top:136px;width:394px;height:199px;background:linear-gradient(100deg,#8fa7b8 0%,#c9b2a0 45%,#b65e66 75%,#a9b86b 100%)}
.video-play{position:absolute;left:157px;top:38px}
.video-controls{position:absolute;left:0;bottom:0;width:100%;height:37px;background:rgba(20,24,28,.75)}
.video-blurb{position:absolute;left:529px;top:344px;width:385px;font-size:12px;line-height:18.4px;font-weight:400}
.learn-more{position:absolute;left:528px;top:412px;display:flex;align-items:center;gap:7px;color:var(--teal);font-size:15px}

.state-search{position:absolute;left:0;top:494px;width:1106px;height:152px;background:var(--teal)}
.search-title{position:absolute;left:151px;top:22px;display:flex;align-items:center;gap:14px;color:var(--white);font-weight:700;font-size:27px;letter-spacing:-.6px}
.select{position:absolute;top:76px;width:262px;height:53px;background:var(--white);color:#a5a9ab;font-weight:300;font-size:20px;padding:13px 0 0 18px}
.select svg{position:absolute;right:21px;top:20px}
.select-state{left:151px}
.select-college{left:422px}
.search-btn{position:absolute;left:692px;top:76px;width:263px;height:53px;background:var(--red);color:var(--white);font-weight:700;font-size:19px;text-align:center;line-height:53px;letter-spacing:-.3px}

.about{position:absolute;left:0;top:646px;width:1106px;height:471px;background:var(--navy);color:var(--white)}
.about-title{position:absolute;left:151px;top:54px;font-weight:700;font-size:27px;letter-spacing:-.5px}
.about-col{position:absolute;top:106px;width:245px;font-size:12.3px;line-height:20.1px;font-weight:400}
.col-1{left:152px}.col-2{left:444px}.col-3{left:713px}
.read-more{position:absolute;left:478px;top:378px;width:151px;height:39px;background:var(--red);color:var(--white);font-weight:700;font-size:12.5px;text-align:center;line-height:39px;letter-spacing:-.3px}

.site-footer{position:absolute;left:0;top:1117px;width:1106px;height:83px;background:var(--footer);color:var(--white);font-family:"Open Sans",Arial,sans-serif;font-size:12px;text-align:center}
.footer-links{margin-top:23px}
.copyright{margin-top:4px}
</style>
</head>
<body>

<div class="topbar">
  <div class="topbar-inner">
    <a class="topbar-link" href="#">About</a>
    <a class="topbar-link" href="#">Contact</a>
    <span class="keep">Keep Connected</span>
    <div class="social"><span></span><span></span><span></span></div>
  </div>
</div>

<header class="site-header">
  <a class="brand" href="#">Quillhaven</a>
  <nav class="main-nav">
    <a class="active" href="#">Home</a>
    <a href="#">States</a>
    <a href="#">Programs</a>
    <a href="#">Degrees</a>
    <a href="#">Accreditation</a>
    <a href="#">Rankings</a>
    <a href="#">Resources</a>
  </nav>
</header>

<section class="definition">
  <h1 class="def-word">ac·cred·it·ed [uh-kred-i-tid]</h1>
  <p class="def-pos">adjective</p>
  <ol class="def-list">
    <li><span class="def-num">1</span><span class="def-text">officially recognized as meeting the essential requirements, as of academic excellence: accredited schools.</span></li>
    <li><span class="def-num">2</span><span class="def-text">provided with official credentials, as by a government: an accredited diplomatic representative</span></li>
    <li><span class="def-num">3</span><span class="def-text">accepted as authoritative: an accredited theory</span></li>
  </ol>
</section>

<div class="video" role="img" aria-label="Video still of smiling students holding notebooks">
  <svg class="video-play" width="80" height="80" viewBox="0 0 80 80"><circle cx="40" cy="40" r="38" fill="rgba(255,255,255,.15)" stroke="rgba(255,255,255,.6)" stroke-width="3"/><path d="M32 26 L56 40 L32 54 Z" fill="rgba(255,255,255,.6)"/></svg>
  <div class="video-controls">
    <svg width="394" height="37" viewBox="0 0 394 37"><path d="M17 13 L26 18.5 L17 24 Z" fill="#8a9196"/><rect x="36" y="17.5" width="260" height="2" fill="#4b5257"/><rect x="36" y="17.5" width="36" height="2" fill="var(--teal)"/><circle cx="72" cy="18.5" r="2.5" fill="var(--teal)"/><rect x="319" y="14" width="2" height="9" fill="#8a9196"/><rect x="323" y="14" width="2" height="9" fill="#8a9196"/><rect x="327" y="14" width="2" height="9" fill="#8a9196"/><rect x="331" y="14" width="2" height="9" fill="#8a9196"/><rect x="370" y="14" width="10" height="9" fill="none" stroke="var(--teal)" stroke-width="1.5" stroke-dasharray="3 4"/></svg>
  </div>
</div>
<p class="video-blurb">Lorem ipsum dolor sit amet, consectetur adipiscing elit. Integer nec odio. Praesent libero. Sed cursus ante dapibus diam. Sed nisi. Nulla quis sem at nibh elementum imperdiet. Duis sagittis ipsum.</p>
<a class="learn-more" href="#"><svg width="20" height="20" viewBox="0 0 20 20"><circle cx="10" cy="10" r="10" fill="var(--teal)"/><path d="M5 8.5h5V5l5 5-5 5v-3.5H5z" fill="#fff"/></svg>Learn more</a>

<section class="state-search">
  <h2 class="search-title"><svg width="48" height="36" viewBox="0 0 48 36"><path d="M24 2 L47 12 L24 22 L1 12 Z" fill="#fff"/><path d="M11 18 V27 C17 33 31 33 37 27 V18 L24 24 Z" fill="#fff"/><rect x="43" y="12" width="2" height="14" fill="#fff"/></svg>Search colleges by state</h2>
  <div class="select select-state">Select a state<svg width="28" height="16" viewBox="0 0 28 16"><path d="M0 0H28L14 16Z" fill="#9aa0a3"/></svg></div>
  <div class="select select-college">Select a college<svg width="28" height="16" viewBox="0 0 28 16"><path d="M0 0H28L14 16Z" fill="#9aa0a3"/></svg></div>
  <a class="search-btn" href="#">SEARCH COLLEGE</a>
</section>

<section class="about">
  <h2 class="about-title">Lorem ipsum dolor sit amet</h2>
  <p class="about-col col-1">consectetur adipiscing elit. Integer nec odio. Praesent libero. Sed cursus ante dapibus diam. Sed nisi. Nulla quis sem at nibh elementum imperdiet. Duis sagittis ipsum. Praesent mauris. Fusce nec tellus sed augue seper porta. Mauris massa. Vestibulum lacinia arcu eget nulla. Class aptent taciti sociosqu ad litora torquent per conubia nostra, per inceptos himenaeos. Curabitur sodales ligula in libero. Sed dignissim lacinia nunc. tristique sem. Proin</p>
  <p class="about-col col-2">consectetur adipiscing elit. Integer nec odio. Praesent libero. Sed cursus ante dapibus diam. Sed nisi. Nulla quis sem at nibh elementum imperdiet. Duis sagittis ipsum. Praesent mauris. Fusce nec tellus sed augue seper porta. Mauris massa. Vestibulum lacinia arcu eget nulla. Class aptent taciti sociosqu ad litora torquent per conubia nostra, per inceptos himenaeos. Curabitur sodales ligula in libero. Sed dignissim lacinia nunc. tristique sem. Proin</p>
  <p class="about-col col-3">consectetur adipiscing elit. Integer nec odio. Praesent libero. Sed cursus ante dapibus diam. Sed nisi. Nulla quis sem at nibh elementum imperdiet. Duis sagittis ipsum. Praesent mauris. Fusce nec tellus sed augue seper porta. Mauris massa. Vestibulum lacinia arcu eget nulla. Class aptent taciti sociosqu ad litora torquent per conubia nostra, per inceptos himenaeos. Curabitur sodales ligula in libero. Sed dignissim lacinia nunc. tristique sem. Proin</p>
  <a class="read-more" href="#">READ MORE</a>
</section>

<footer class="site-footer">
  <p class="footer-links"><a href="#">About us</a> | <a href="#">Privacy Information</a> | <a href="#">Site Map</a></p>
  <p class="copyright">© Copyright 2013 - &nbsp;All Right Reserved</p>
</footer>

</body>
</html>
```